CustomerPath UX Overhaul - redesign to improve visitor journeys and conversions

I need my website brought to life, professional and engaging.
I can supply as much pictures as needed to create enhancing visuals. I need your team to review the website and create a list of ideas of what you need from me to bring this vision to life.
The company does 3d modeling, 3d printing with FDM and resin printers, CAD design, 3d scanning.
My website is https://qtforgeworks.com/
Please review it and give me your best.
Target Market(s)
cosplayer, filmmakers, life size prints, custom designs, redesign and scanning, large and small scale prints, replicating
Industry/Entity Type
CAD Design, Additive Manufacturing, 3D Printing, 3D Scanning
Coding
Coded - Design and coding required
Number of Pages Required
3 page
Requirements
Must have
- Professional and clean look, inviting, eye grabber

```html
<!DOCTYPE html>
<html lang="en">
<head>
<meta charset="utf-8">
<title>QT Forgeworks – 3D Printing, Modelling &amp; Scanning</title>
<link href="https://fonts.googleapis.com/css2?family=Inter:wght@400;500;600;700&display=swap" rel="stylesheet">
<style>
:root{
  --backdrop:#9c9c9c;
  --navy-top:#0d1230;
  --navy-1:#0b1130;
  --navy-2:#070d2a;
  --card:#0f1638;
  --ink-dark:#0a0f2a;
  --accent:#27a3dc;
  --accent-text:#2ba9e4;
  --white:#ffffff;
  --muted:#c9cfdf;
}
*{box-sizing:border-box;margin:0;padding:0}
html,body{width:833px;height:1200px;overflow:hidden;background:var(--backdrop);font-family:"Inter",sans-serif;color:var(--white)}
.page{position:absolute;left:56px;top:56px;width:721px;height:1087px;background:var(--navy-2);box-shadow:0 6px 18px rgba(0,0,0,.25);overflow:hidden}
.hero{position:absolute;left:0;top:0;width:721px;height:405px;border-top:4px solid var(--navy-top)}
.hero-photo{position:absolute;inset:0;background:
  radial-gradient(ellipse at 88% 12%,#f6d08a 0%,rgba(224,160,80,.7) 18%,rgba(0,0,0,0) 45%),
  radial-gradient(ellipse at 30% 45%,#3f86c4 0%,#2b5f92 30%,rgba(0,0,0,0) 60%),
  radial-gradient(ellipse at 70% 85%,#efe2c4 0%,#d7c09a 25%,rgba(0,0,0,0) 55%),
  linear-gradient(90deg,#3c4a52 0%,#7a6a4e 55%,#c79a5c 100%)}
.brand{position:absolute;left:10px;top:14px;display:flex;align-items:center;gap:6px}
.brand-dot{width:28px;height:28px;border-radius:50%;background:var(--accent)}
.brand-name{font-weight:600;font-size:11px;color:var(--white)}
.nav{position:absolute;right:9px;top:12px;display:flex;align-items:center;font-size:7.6px;font-weight:600;color:var(--ink-dark)}
.nav a{color:inherit;text-decoration:none;margin-left:18px}
.nav a:nth-child(3){margin-left:12px}
.nav .nav-cta{background:var(--accent);padding:6px 8px;margin-left:9px;color:var(--ink-dark)}
.hero-copy{position:absolute;left:0;right:0;top:152px;text-align:center}
.hero-title{font-size:27px;font-weight:700;letter-spacing:-.2px}
.hero-sub{font-size:9.4px;line-height:13px;margin-top:3px}
.hero-actions{position:absolute;top:227px;left:261px;display:flex;gap:8px}
.btn{display:block;width:96px;height:28px;line-height:28px;text-align:center;font-weight:600;font-size:9.4px;text-decoration:none}
.btn-dark{background:var(--ink-dark);color:var(--accent-text)}
.btn-accent{background:var(--accent);color:var(--ink-dark);width:95px}
.section-title{text-align:center;font-size:12.5px;font-weight:700}
.services{position:absolute;top:405px;left:0;width:721px;height:186px;background:var(--navy-1)}
.services .section-title{margin-top:28px}
.service-grid{position:absolute;left:139px;top:57px;display:flex;gap:1px}
.service-card{width:110px;height:103px;background:var(--card);border-radius:3px;padding:14px 13px}
.service-card h3{font-size:8px;line-height:13px;font-weight:600;color:var(--accent-text);margin-bottom:6px}
.service-card p{font-size:6.3px;line-height:9px}
.work{position:absolute;top:591px;left:0;width:721px}
.work .section-title{margin-top:30px}
.work-grid{position:absolute;left:139px;top:56px;display:flex;gap:7px}
.work-item{width:68.5px;height:74px;border-radius:2px}
.w1{background:linear-gradient(#eeeeec,#cfcfcd)}
.w2{background:linear-gradient(135deg,#e6eef6,#b7c8dc)}
.w3{background:linear-gradient(135deg,#2a2c34,#111218 60%,#3a48a8)}
.w4{background:linear-gradient(#1c2d52 0 18%,#f4f6fa 18%)}
.w5{background:linear-gradient(135deg,#d9cdb6,#7d8590 50%,#e8e4df)}
.w6{background:linear-gradient(#1c5fbf 0 14%,#f6f8fb 14%)}
.about{position:absolute;top:786px;left:0;width:721px}
.about-text{position:absolute;left:139px;top:23px;width:446px;font-size:6.7px;line-height:10.4px}
.stats{position:absolute;top:48px;left:0;width:721px}
.stat{position:absolute;width:140px;text-align:center;color:var(--accent-text)}
.stat b{display:block;font-size:13.5px;font-weight:700}
.stat span{display:block;font-size:7px;margin-top:3px}
.tags{position:absolute;top:83px;left:285px;display:flex;gap:3px}
.tag{font-size:5px;color:var(--accent-text);border:1px solid var(--accent);border-radius:2px;height:13px;line-height:11px;padding:0 5px}
.cta{position:absolute;top:935px;left:0;width:721px;text-align:center}
.cta p{font-size:7px;margin-top:15px}
.cta .btn-small{display:inline-block;margin-top:10px;background:var(--accent);color:var(--white);font-size:6.6px;font-weight:600;width:73px;height:21px;line-height:21px;border-radius:2px;text-decoration:none}
.footer{position:absolute;top:1049px;left:0;width:721px;text-align:center;font-size:5.3px;line-height:8.3px;color:var(--muted)}
.footer a{color:var(--accent-text);text-decoration:none}
</style>
</head>
<body>
<div class="page">
  <header class="hero">
    <div class="hero-photo" role="img" aria-label="Photo of a technician in a blue lab coat and safety glasses assembling a 3D-printed city skyline model in a sunlit workshop"></div>
    <div class="brand"><span class="brand-dot"></span><span class="brand-name">QT Forgeworks</span></div>
    <nav class="nav">
      <a href="#">HOME</a><a href="#">ABOUT</a><a href="#">SERVICES &amp; SPECS</a><a class="nav-cta" href="#">REQUEST A QUOTE</a>
    </nav>
    <div class="hero-copy">
      <h1 class="hero-title">Bring your ideas to life in 3D</h1>
      <p class="hero-sub">Custom 3D printing, modelling and scanning services for cosplayers, filmmakers,<br>engineers and makers. From tiny prototypes to life-size props, we make it real.</p>
    </div>
    <div class="hero-actions">
      <a class="btn btn-dark" href="#">Request a Quote</a>
      <a class="btn btn-accent" href="#">See Our Work</a>
    </div>
  </header>

  <section class="services">
    <h2 class="section-title">What we do</h2>
    <div class="service-grid">
      <article class="service-card"><h3>FDM &amp; Resin Printing</h3><p>High-precision FDM and resin printing with layer heights down to 50 µm. Build volumes up to 400×400×400 mm in a single piece.</p></article>
      <article class="service-card"><h3>CAD Design &amp;<br>Modelling</h3><p>We transform sketches and ideas into manufacturable CAD models, ready for printing or downstream production.</p></article>
      <article class="service-card"><h3>3D Scanning &amp;<br>Reverse Engineering</h3><p>Capture real-world objects with handheld scanners for modification, replication or digital archiving.</p></article>
      <article class="service-card"><h3>Post-Processing &amp;<br>Finishing</h3><p>Support removal, sanding, painting, vapor smoothing, inserts and assembly to meet your desired finish and tolerance.</p></article>
    </div>
  </section>

  <section class="work">
    <h2 class="section-title">Recent work</h2>
    <div class="work-grid">
      <div class="work-item w1" role="img" aria-label="Grey printed miniature of a cloaked knight with a sword"></div>
      <div class="work-item w2" role="img" aria-label="CAD render of a mechanical bracket on a blueprint grid"></div>
      <div class="work-item w3" role="img" aria-label="Hand holding a handheld 3D scanner"></div>
      <div class="work-item w4" role="img" aria-label="Website page preview with services and recent work"></div>
      <div class="work-item w5" role="img" aria-label="Collage of printed figures, parts and colourful prints"></div>
      <div class="work-item w6" role="img" aria-label="Website page preview with services grid and process"></div>
    </div>
  </section>

  <section class="about">
    <h2 class="section-title">About us</h2>
    <p class="about-text">We’re a family-run production shop in Maple Falls, Vermont focussed on service, precision and clear communication. From one-off prototypes to short-run production, we help you choose the right process and deliver on time.</p>
    <div class="stats">
      <div class="stat" style="left:138px"><b>3000+</b><span>parts printed</span></div>
      <div class="stat" style="left:290px"><b>120+</b><span>happy clients</span></div>
      <div class="stat" style="left:443px"><b>3–5 d</b><span>typical lead time</span></div>
    </div>
    <div class="tags"><span class="tag">Veteran support</span><span class="tag">Made in VT</span><span class="tag">QC report provided</span></div>
  </section>

  <section class="cta">
    <h2 class="section-title">Ready to start your project?</h2>
    <p>Upload your files and tell us about your goals. We’ll review and reply within 24–48 business hours.</p>
    <a class="btn-small" href="#">Request a Quote</a>
  </section>

  <footer class="footer">
    © 2025 QT Forgeworks Studio. All rights reserved.<br>
    <a href="#">hello@qtforgeworks.com</a> &nbsp;|&nbsp; Maple Falls, VT – Production only<br>
    Licensed &amp; insured. Veteran discount: 10% on labour.
  </footer>
</div>
</body>
</html>
```